Modern Innovative Business Card Design

We require a nice, modern, clean business card design, ready for upload to Cardwello. Our company develops online banking software solutions for small financial insitutions. The design should be clean, professional, but yet not "corporate boring". See www.fintrola.com for an idea of business image and profile. The design should communicate innovation, be modern and fresh, yet look professional and established.

Target Market(s)

Finance industry, bankers, entrepreneurs

Industry/Entity Type

Financial

Contact Information for Business Card

Daniel Hargreave
CEO

FINTROLA BV
Lindenhofstraat 38
1072 KD Amsterdam
The Netherlands

Phone: +31 20 517 8063
Direct: +31 20 446 1975
Skype: daniel.fintrola
ceo@fintrola.com
www.fintrola.com

Font styles to use
Sans Serif

Requirements
Must have
• Should look clean, modern and professional. File should be ready for upload to cardwello.
Should not have
• Boring standard corporate layout

```html
<!DOCTYPE html>
<html lang="en">
<head>
<meta charset="utf-8">
<title>FINTROLA Business Card</title>
<link rel="stylesheet" href="https://fonts.googleapis.com/css2?family=Lato:wght@400;700;900&display=swap">
<style>
:root{
  --backdrop:#2b2b2b;
  --card:#ffffff;
  --slate:#3a4346;
  --slate-edge:#cfd3d4;
  --lime:#8cc63f;
  --ink:#5b5f61;
  --light:#e8ecec;
}
*{margin:0;padding:0;box-sizing:border-box}
html,body{width:1200px;height:997px;overflow:hidden;background:var(--backdrop)}
body{position:relative;font-family:"Lato",sans-serif}
.card{position:absolute;left:150px;top:241px;width:900px;height:514px;background:var(--card);overflow:hidden;box-shadow:0 18px 40px rgba(0,0,0,.5)}
.brand{position:absolute;left:180px;top:110px;display:flex;align-items:center;gap:18px}
.brand-square{width:38px;height:38px;background:var(--lime)}
.brand-name{font-weight:700;font-size:76px;letter-spacing:4px;color:var(--ink);line-height:1}
.accent-block{position:absolute;left:760px;top:150px;width:140px;height:260px;background:var(--lime)}
.info-panel{position:absolute;left:70px;top:198px;width:700px;height:226px;background:var(--slate);border:5px solid var(--slate-edge)}
.holder{position:absolute;right:22px;top:10px;text-align:right;color:var(--light)}
.holder-name{font-weight:900;font-size:27px}
.holder-title{font-size:16px;margin-top:-2px}
.contacts{position:absolute;left:18px;bottom:10px;list-style:none;color:var(--light);font-size:20px;line-height:36px}
.icon-strip{position:absolute;left:0;top:272px;width:52px;height:150px;background:var(--lime);display:flex;flex-direction:column;justify-content:space-around;align-items:center;padding:6px 0}
.icon-strip svg{width:20px;height:20px;fill:var(--slate)}
.rule{position:absolute;left:0;right:0;top:444px;height:4px;background:var(--lime)}
.footer-band{position:absolute;left:0;right:0;top:452px;bottom:0;background:var(--slate);color:var(--light);font-weight:700;font-size:17px;display:flex;align-items:center;padding-left:150px}
</style>
</head>
<body>
<div class="card">
  <div class="brand">
    <span class="brand-square"></span>
    <span class="brand-name">FINTROLA</span>
  </div>
  <div class="accent-block"></div>
  <div class="info-panel">
    <div class="holder">
      <div class="holder-name">Daniel Hargreave</div>
      <div class="holder-title">CEO</div>
    </div>
    <ul class="contacts">
      <li>+31 20 446 1975</li>
      <li>+31 20 517 8063</li>
      <li>daniel.fintrola</li>
      <li>ceo@fintrola.com</li>
    </ul>
  </div>
  <div class="icon-strip">
    <svg viewBox="0 0 24 24" aria-label="phone"><path d="M6.6 10.8a15 15 0 0 0 6.6 6.6l2.2-2.2c.3-.3.7-.4 1-.2 1.1.4 2.3.6 3.6.6.6 0 1 .4 1 1V20c0 .6-.4 1-1 1A17 17 0 0 1 3 4c0-.6.4-1 1-1h3.5c.6 0 1 .4 1 1 0 1.3.2 2.5.6 3.6.1.3 0 .7-.2 1z"/></svg>
    <svg viewBox="0 0 24 24" aria-label="direct line"><path d="M6.6 10.8a15 15 0 0 0 6.6 6.6l2.2-2.2c.3-.3.7-.4 1-.2 1.1.4 2.3.6 3.6.6.6 0 1 .4 1 1V20c0 .6-.4 1-1 1A17 17 0 0 1 3 4c0-.6.4-1 1-1h3.5c.6 0 1 .4 1 1 0 1.3.2 2.5.6 3.6.1.3 0 .7-.2 1z"/></svg>
    <svg viewBox="0 0 24 24" aria-label="chat"><path d="M4 4h16a1 1 0 0 1 1 1v10a1 1 0 0 1-1 1H9l-5 4v-4a1 1 0 0 1-1-1V5a1 1 0 0 1 1-1z"/></svg>
    <svg viewBox="0 0 24 24" aria-label="email"><path d="M3 5h18v14H3z M3 5l9 7 9-7" stroke="#8cc63f" stroke-width="1.5"/></svg>
  </div>
  <div class="rule"></div>
  <div class="footer-band">FINTROLA BV Lindenhofstraat 38 1072 KD&nbsp; Amsterdam The Netherlands</div>
</div>
</body>
</html>
```